Plakat-Design für Frauenfitnessstudio
Zielgruppe
Frauenfitnessstudio
Aufgabenstellung
Wir benötigen eine Außenplane die an der eingezeichneten Postion befestigt werden soll (Anhang 'Außenansicht').
Auf der Plane soll mindestens folgender Inhalt dargestellt werden:
- Logo
- Website 'morvenhalle-augsburg.de'
- Trelvano-Logo
- Pixomerat-Logo
Die Plane soll ab einer Reichweite von ca. 50 Metern erkennbar sein.
Die Maße betragen 480x280 cm.

```html
<!DOCTYPE html>
<html lang="de">
<head>
<meta charset="utf-8">
<title>Morvenhalle – Wohlfühl-Fitness für die Frau</title>
<link href="https://fonts.googleapis.com/css2?family=Open+Sans:wght@300;400;700&display=swap" rel="stylesheet">
<style>
  :root {
    --orange: #f05d22;
    --pink: #e1408c;
    --pink-soft: #f06aa8;
    --orange-soft: #f3793a;
    --white: #ffffff;
    --brand-gold: #f4a11d;
    --photo-light: #efe6dc;
    --photo-warm: #e9c3a0;
  }
  html, body {
    margin: 0;
    padding: 0;
    overflow: hidden;
    background: var(--white);
  }
  .banner {
    position: relative;
    width: 1200px;
    height: 700px;
    overflow: hidden;
    background: var(--white);
    font-family: "Open Sans", Arial, sans-serif;
  }
  .banner__art {
    position: absolute;
    inset: 0;
  }
  .headline {
    position: absolute;
    margin: 0;
    color: var(--white);
    font-weight: 700;
    line-height: 1;
    white-space: nowrap;
  }
  .headline--top {
    left: 44px;
    top: 45px;
    font-size: 136px;
    letter-spacing: -1px;
  }
  .headline--fit {
    left: 282px;
    top: 163px;
    font-size: 136px;
  }
  .highlight-box {
    position: absolute;
    left: 36px;
    top: 158px;
    width: 232px;
    height: 138px;
    border: 5px solid var(--white);
    transform: rotate(-5deg);
    box-sizing: border-box;
  }
  .highlight-box__word {
    position: absolute;
    left: 14px;
    top: -2px;
    color: var(--white);
    font-weight: 700;
    font-size: 130px;
    line-height: 1;
  }
  .subline {
    position: absolute;
    left: 46px;
    top: 336px;
    margin: 0;
    color: var(--white);
    font-weight: 400;
    font-size: 67px;
    line-height: 60px;
    letter-spacing: 0.5px;
  }
  .contact {
    position: absolute;
    left: 44px;
    top: 530px;
    color: var(--pink);
    font-weight: 300;
    font-size: 55px;
    line-height: 62px;
    white-space: nowrap;
  }
  .contact p { margin: 0; }
  .social {
    position: absolute;
    left: 816px;
    top: 598px;
    display: flex;
    flex-direction: column;
    gap: 10px;
  }
  .social__item {
    display: flex;
    align-items: center;
    gap: 7px;
    color: var(--pink);
    font-weight: 700;
    font-size: 15px;
    line-height: 22px;
    white-space: nowrap;
  }
  .social__dot {
    flex: none;
    width: 22px;
    height: 22px;
    border-radius: 50%;
    background: var(--pink);
  }
  .brand {
    position: absolute;
    left: 965px;
    top: 550px;
    margin: 0;
    color: var(--brand-gold);
    font-weight: 700;
    font-size: 44px;
    line-height: 50px;
    text-align: center;
    width: 200px;
  }
</style>
</head>
<body>
<main class="banner">
  <svg class="banner__art" width="1200" height="700" viewBox="0 0 1200 700">
    <defs>
      <clipPath id="top-band"><rect x="0" y="0" width="1200" height="494"/></clipPath>
      <radialGradient id="photo-tone" cx="0.6" cy="0.4" r="0.7">
        <stop offset="0" stop-color="#e9c3a0"/>
        <stop offset="1" stop-color="#efe6dc"/>
      </radialGradient>
    </defs>
    <rect class="band band--orange" x="0" y="0" width="1200" height="494" fill="var(--orange)"/>
    <g clip-path="url(#top-band)">
      <circle class="bubble bubble--pink" cx="912" cy="158" r="245" fill="var(--pink)"/>
      <circle class="bubble bubble--orange-soft" cx="1154" cy="101" r="158" fill="var(--orange-soft)" opacity="0.85"/>
      <circle class="bubble bubble--pink-soft" cx="1085" cy="307" r="144" fill="var(--pink-soft)" opacity="0.85"/>
    </g>
    <circle class="photo" cx="898" cy="377" r="149" fill="url(#photo-tone)" role="img" aria-label="Foto: lächelnde Frau im gelben Top beim Training mit Kurzhantel"/>
  </svg>

  <h1 class="headline headline--top">WIR MACHEN</h1>
  <div class="highlight-box"><span class="highlight-box__word">SIE</span></div>
  <div class="headline headline--fit">FIT!</div>

  <h2 class="subline">WOHLFÜHL-FITNESS<br>FÜR DIE FRAU</h2>

  <div class="contact">
    <p class="contact__phone">0821-564120</p>
    <p class="contact__web">www.morvenhalle-augsburg.de</p>
  </div>

  <div class="social">
    <span class="social__item"><span class="social__dot"></span>Trelvano</span>
    <span class="social__item"><span class="social__dot"></span>Pixomerat</span>
  </div>

  <p class="brand">MORVEN<br>HALLE</p>
</main>
</body>
</html>
```